Broschüre Personalberatung
Zielgruppe
Personalberatung im technischen Umfeld für Führungskräfte und spezialisierte Experten
Aufgabenstellung
Es soll eine neue Firmenpräsentation für PDF Versand designt werden. Nur das Design der Seiten mit Kästen für Texte. Es sollen die Rauten / eckigen Kanten die um das Logo herum sind sich wieder in dem Layout wiederfinden. Die Deckseite von der angehängten Firmenpräsentation finde ich z.B. nicht schlecht. Keine Runden Elemente, gerne klare Linien wie in den Beispielen unten. Das Layout muss zum Schluss in Canva bereitgestellt werden, damit wir es auch weiter bearbeiten können. Die Farben sollen sich aus dem logo und dem generellen Auftritt wieder finden können. Stil soll seriös und professionell sein

```html
<!DOCTYPE html>
<html lang="de">
<head>
<meta charset="utf-8">
<title>Recruiting ohne Floskeln – Velora executive</title>
<link rel="stylesheet" href="https://fonts.googleapis.com/css2?family=Open+Sans:wght@400;600;700;800&display=swap">
<style>
  :root{
    --navy:#141d4a;
    --blue:#2a8fbd;
    --slate:#474d57;
    --ink:#161616;
    --text:#252525;
    --rule:#5b5b5b;
    --stage:#d9dbde;
    --paper:#ffffff;
    --footer:#e8eaed;
  }
  *{margin:0;padding:0;box-sizing:border-box}
  html,body{width:1200px;height:1200px;overflow:hidden}
  body{background:var(--stage);font-family:"Open Sans",Arial,sans-serif;color:var(--text);position:relative}
  .page{position:absolute;left:165px;top:20px;width:870px;height:1160px;background:var(--paper);overflow:hidden}
  .page-frame{position:absolute;inset:0}
  .footer-band{position:absolute;left:0;right:0;bottom:0;height:90px;background:linear-gradient(180deg,var(--paper),var(--footer))}
  .title-block{position:absolute;left:130px;top:118px;display:flex;align-items:center;gap:26px}
  .title-mark{width:34px;height:34px;background:var(--blue)}
  .title{font-weight:800;font-size:38px;line-height:1.05;letter-spacing:.5px}
  .title .line-1{color:var(--navy);display:block}
  .title .line-2{color:var(--slate);display:block;padding-left:10px}
  .title-rule{position:absolute;left:140px;top:240px;width:640px;height:1px;background:var(--rule)}
  .intro{position:absolute;left:245px;top:318px;font-size:15px;color:var(--ink)}
  .hack{position:absolute;display:flex;align-items:center;gap:22px}
  .hack-hex{width:112px;height:92px;flex:none}
  .hack-title{font-weight:800;font-size:21px;color:var(--ink);letter-spacing:.3px;margin-bottom:4px}
  .hack-text{font-size:17px;line-height:1.3;color:var(--text)}
  .hack-1{left:250px;top:390px}
  .hack-2{left:292px;top:525px}
  .hack-3{left:334px;top:660px}
  .hack-4{left:376px;top:795px}
  .footer{position:absolute;left:0;right:0;bottom:22px;height:40px;font-size:11px;line-height:1.25;color:var(--ink)}
  .brand{position:absolute;left:155px;top:6px;display:flex;align-items:center;gap:6px;font-size:15px;font-weight:600;color:var(--navy)}
  .brand-mark{width:10px;height:10px;background:var(--navy)}
  .contact{position:absolute;left:430px;top:4px}
  .address{position:absolute;left:600px;top:4px}
</style>
</head>
<body>
  <main class="page">
    <div class="footer-band"></div>
    <svg class="page-frame" viewBox="0 0 870 1160" width="870" height="1160" aria-hidden="true">
      <polygon points="0,0 870,0 870,22 0,22" fill="var(--blue)"/>
      <polygon points="0,34 790,34 802,52 0,52" fill="var(--navy)"/>
      <polygon points="775,0 815,0 870,90 870,150" fill="var(--navy)"/>
      <polygon points="828,0 870,0 870,68" fill="var(--blue)"/>
      <polygon points="0,1118 45,1118 70,1160 0,1160" fill="var(--blue)"/>
      <polygon points="0,1096 90,1096 128,1160 96,1160 70,1114 0,1114" fill="var(--navy)"/>
    </svg>

    <header class="title-block">
      <span class="title-mark"></span>
      <h1 class="title"><span class="line-1">RECRUITING</span><span class="line-2">OHNE FLOSKELN</span></h1>
    </header>
    <div class="title-rule"></div>

    <p class="intro">4 Einfache Hacks Aus Der Praxis:</p>

    <section class="hack hack-1">
      <svg class="hack-hex" viewBox="0 0 112 92" aria-hidden="true">
        <path d="M52,7 H27 L8,46 L27,85 H70" fill="none" stroke="var(--navy)" stroke-width="9"/>
        <path d="M66,5 H80 L102,45 L84,83" fill="none" stroke="var(--blue)" stroke-width="6"/>
        <rect x="44" y="36" width="20" height="20" fill="var(--blue)"/>
      </svg>
      <div><h2 class="hack-title">VERSTÄNDNIS</h2><p class="hack-text">Wir besetzen keine Stellen –<br>wir lösen die eigentliche Aufgabe.</p></div>
    </section>

    <section class="hack hack-2">
      <svg class="hack-hex" viewBox="0 0 112 92" aria-hidden="true">
        <path d="M52,7 H27 L8,46 L27,85 H70" fill="none" stroke="var(--navy)" stroke-width="9"/>
        <path d="M66,5 H80 L102,45 L84,83" fill="none" stroke="var(--blue)" stroke-width="6"/>
        <circle cx="56" cy="46" r="14" fill="none" stroke="var(--blue)" stroke-width="3"/>
        <circle cx="56" cy="46" r="6" fill="var(--navy)"/>
      </svg>
      <div><h2 class="hack-title">ANALYSE</h2><p class="hack-text">Nicht der Lebenslauf zählt zuerst,<br>sondern das Problem dahinter.</p></div>
    </section>

    <section class="hack hack-3">
      <svg class="hack-hex" viewBox="0 0 112 92" aria-hidden="true">
        <path d="M52,7 H27 L8,46 L27,85 H70" fill="none" stroke="var(--navy)" stroke-width="9"/>
        <path d="M66,5 H80 L102,45 L84,83" fill="none" stroke="var(--blue)" stroke-width="6"/>
        <rect x="40" y="34" width="12" height="24" fill="var(--blue)"/>
        <rect x="58" y="34" width="12" height="24" fill="var(--navy)"/>
      </svg>
      <div><h2 class="hack-title">PASSUNG</h2><p class="hack-text">Nicht viele Profile – sondern die<br>richtigen mit echter Passung zur Aufgabe.</p></div>
    </section>

    <section class="hack hack-4">
      <svg class="hack-hex" viewBox="0 0 112 92" aria-hidden="true">
        <path d="M52,7 H27 L8,46 L27,85 H70" fill="none" stroke="var(--navy)" stroke-width="9"/>
        <path d="M66,5 H80 L102,45 L84,83" fill="none" stroke="var(--blue)" stroke-width="6"/>
        <polygon points="38,34 74,34 58,62" fill="none" stroke="var(--navy)" stroke-width="3"/>
        <polygon points="50,38 70,38 58,58" fill="var(--blue)"/>
      </svg>
      <div><h2 class="hack-title">KLARHEIT</h2><p class="hack-text">Transparente Prozesse schaffen<br>Vertrauen und bessere Entscheidungen.</p></div>
    </section>

    <footer class="footer">
      <div class="brand"><span class="brand-mark"></span>Velora executive</div>
      <div class="contact">info@velora-beispiel.de<br>(089) 123 45 67 0</div>
      <div class="address">www.velora-beispiel.de<br>Musterstraße 12, 80000 München</div>
    </footer>
  </main>
</body>
</html>
```